Party flyer design

Hi ArtHive,

I need a party flyer designed incorporating my logo and the verbiage stated below for a
social get-together I'm throwing at a local martini bar and lounge in my local area.

I've attached my logo and a copy of a flyer I've seen that incorporates the look and feel I'm looking for.

Thanks

Lumora 4 presents
Velvet Hour Mixers

Join us Fridays at 11:00 PM - 2:00 AM
at At The Quill Westbrook
27315 Harlow Ridge, Suite 340
Charlotte, NC 28193

For more details email us at info@lumora4.com

```html
<!DOCTYPE html>
<html lang="en">
<head>
<meta charset="utf-8">
<title>Lumora 4 — Velvet Hour Mixers</title>
<link rel="stylesheet" href="https://fonts.googleapis.com/css2?family=Great+Vibes&family=Frijole&family=Crimson+Text:wght@700&display=swap">
<style>
  :root {
    --paper: #fbfaf9;
    --paper-edge: #e6e3e0;
    --orange: #f0701f;
    --orange-deep: #d4560e;
    --ink: #161616;
    --title-blue: #2b5f8c;
    --address: #c4521a;
    --photo-top: #d9cfc8;
    --photo-mid: #6b4f44;
    --splash: #9ed3ee;
    --speaker: #2a2a2a;
    --speaker-rim: #555;
  }
  * { margin: 0; padding: 0; box-sizing: border-box; }
  html, body { width: 849px; height: 1200px; overflow: hidden; }
  body { background: #fff; }
  .flyer {
    position: relative;
    width: 849px; height: 1200px;
    overflow: hidden;
    background: radial-gradient(ellipse at 50% 45%, var(--paper) 55%, var(--paper-edge) 100%);
    font-family: "Crimson Text", Georgia, serif;
  }
  .brand {
    position: absolute; top: 6px; left: 0; width: 100%;
    text-align: center;
  }
  .brand-dot {
    display: block; margin: 0 auto;
    width: 96px; height: 96px; border-radius: 50%;
    background: var(--orange);
  }
  .brand-name {
    display: block;
    font-family: "Great Vibes", cursive;
    font-size: 62px; line-height: 1; margin-top: 4px;
    color: var(--ink);
  }
  .presents {
    position: absolute; top: 258px; left: 440px;
    font-family: "Great Vibes", cursive;
    font-size: 40px; line-height: 1; color: var(--ink);
    z-index: 2;
  }
  .photo {
    position: absolute; left: 220px; top: 235px; width: 460px; height: 410px;
    border-radius: 46% 46% 18% 18%;
    background: linear-gradient(180deg, var(--photo-top) 0%, var(--photo-mid) 40%, var(--ink) 100%);
    opacity: 0.9;
  }
  .splash {
    position: absolute; left: 40px; top: 390px; width: 780px; height: 180px;
    border-radius: 50%;
    background: radial-gradient(ellipse at center, var(--splash) 0%, rgba(158,211,238,0.5) 45%, rgba(158,211,238,0) 70%);
  }
  .speaker { position: absolute; background: linear-gradient(135deg, var(--speaker-rim), var(--speaker)); border-radius: 10px; }
  .speaker-left { left: -20px; top: 690px; width: 160px; height: 350px; transform: skewY(6deg); }
  .speaker-right { left: 718px; top: 935px; width: 150px; height: 290px; transform: skewY(-6deg); }
  .title {
    position: absolute; top: 528px; left: 0; width: 100%;
    text-align: center;
    font-family: "Frijole", fantasy;
    font-weight: 400;
    line-height: 1;
    z-index: 2;
  }
  .title-line1 { display: block; font-size: 76px; color: var(--ink); letter-spacing: -2px; }
  .title-line2 { display: block; font-size: 96px; color: var(--title-blue); margin-top: 14px; }
  .details {
    position: absolute; top: 830px; left: 150px; width: 549px;
    text-align: center; color: var(--orange);
    font-weight: 700;
    z-index: 2;
  }
  .join { font-size: 38px; line-height: 1.1; }
  .when { font-size: 36px; line-height: 1.25; white-space: nowrap; }
  .venue { font-size: 44px; line-height: 1.25; margin-top: 8px; color: var(--orange-deep); white-space: nowrap; }
  .address { font-size: 36px; line-height: 1.2; color: var(--address); white-space: nowrap; }
  .contact { font-size: 23px; margin-top: 22px; white-space: nowrap; }
</style>
</head>
<body>
<main class="flyer">
  <header class="brand">
    <span class="brand-dot"></span>
    <span class="brand-name">Lumora 4</span>
  </header>

  <div class="photo" role="img" aria-label="Photo of two glamorous women in black party outfits"></div>
  <div class="splash" role="img" aria-label="Blue water splash sweeping across the image"></div>
  <div class="presents">Presents</div>

  <div class="speaker speaker-left" role="img" aria-label="Black loudspeaker"></div>
  <div class="speaker speaker-right" role="img" aria-label="Black loudspeaker"></div>

  <h1 class="title">
    <span class="title-line1">Velvet Hour</span>
    <span class="title-line2">Mixers</span>
  </h1>

  <section class="details">
    <p class="join">Join us</p>
    <p class="when">Fridays at 11:00 PM - 2:00 AM</p>
    <p class="venue">@ At The Quill Westbrook</p>
    <p class="address">27315 Harlow Ridge, Suite 340</p>
    <p class="address">Charlotte, NC 28193</p>
    <p class="contact">For more details email us at info@lumora4.com</p>
  </section>
</main>
</body>
</html>
```